Business Card for a Candle Company. - Creative Hipster Styling :)

I am after a two sided Business Card. Contact information on the front, text that will be supplied (and details further on here) on the back. Ideally I am looking for someone I can continue to work with in the future for flyers, labels, marketing material etc.

I have a Logo which I am using as the labels for the candle and have attached all the versions of the file I was given. I am after a similar feel to my logo and love the font and the feather used. it is important that my card looks like it is meant to go with the logo.

I would love you to use your imagination and see what can be thought up :)

All my candles are either clear or black glass and packaging is black and labels are white, on a square label with black writing (see attachments)

I love the feather on the logo if it can be incorporated great, if the business card looks better without it than that is fine too..

Target Market(s)

I am a new candle company and the feel I'm going for is a little luxury a little hipster. Imagine the candle going into a converted warehouse studio in the city.

Industry/Entity Type

Home And Garden

Contact Information for Business Card

I have a Logo which I am using as the labels for the candle and have attached all the versions of the file I was given. I am after a similar feel to my logo and love the font used but its caps and I don't really want everything in CAPS. It is important thought that everything goes together.

I love the feather on the logo if it can be incorporated great, if the business card looks better without it than that is fine too.

Morrel Wick Co
Saltmarsh Bay, NSW Australia
A small wax studio, in a shed, by the bay.
craftlane.example/au/shop/MorrelWickCo
friendspace.example.au/morrelwickco
morrelwickco@mailbox.example.au
Jess Holloran
0481 572 316.

On the back of the card I need it to look good and go with the design on the front but want a bit of text;

To give you an idea of what I want on the back I've put what I've got following but I'm still working on grammar and wording so it may change slightly before the final edit.

We would love to see how you display your candle or reuse the glass vessel and would love to see a photo!
Check out ideas and share yours on your social media #morrelwickco

Just a few ideas to reuse your vessel;

A Vase to Display fresh flowers
Lolly Jar for your favourite candy
Decorate with baubles at Christmas
Bathroom Vanity Storage
Decorate with eggs at Easter
Plant a teranium inside.

Font styles to use
Decorative
Script
Other font styles liked:
• OctinVintageFree

Colors
000000
ffffff
757575

Requirements
Must have
• The only must is that it needs to look like it goes with my logo which I am using as the labels on the actual candle. the labels are white with black details and are square.
• Not too structured if possible as it is a creative company rather that a professional services company.
• I want people to pick up the card and think it looks great. I believe a business card is a very useful marketing tool and should be used as such. One card will be included in with each candle so that customers can re order.
Nice to have
• I love the feather on the logo if it can be incorporated great, if the business card looks better without it than that is fine too.
• Card just needs to fit with the logo.
Should not have
• It should not be a boring card. :)

```html
<!DOCTYPE html>
<html lang="en">
<head>
<meta charset="utf-8">
<title>Morrel Wick Co – Business Card</title>
<link href="https://fonts.googleapis.com/css2?family=Roboto+Slab:wght@300;400;700&display=swap" rel="stylesheet">
<style>
  :root {
    --ink: #000000;
    --paper: #ffffff;
    --bronze: #5a3f2e;
    --grey: #757575;
    --stage: #e9e6e2;
  }
  * { margin: 0; padding: 0; box-sizing: border-box; }
  html, body { width: 1200px; height: 913px; overflow: hidden; background: var(--stage); }
  .canvas { position: relative; width: 1200px; height: 913px; font-family: "Roboto Slab", serif; }
  .card {
    position: absolute; width: 560px; height: 320px; border-radius: 16px;
    overflow: hidden; background: var(--paper);
    box-shadow: 0 10px 30px rgba(0,0,0,.22);
  }
  .card-front { left: 30px; top: 296px; }
  .card-back { left: 610px; top: 296px; }
  .card svg.waves { position: absolute; inset: 0; }

  .holder { position: absolute; left: 28px; top: 74px; }
  .holder-name { font-weight: 700; font-size: 22px; color: var(--ink); }
  .holder-role { font-size: 14px; color: var(--bronze); margin-top: 2px; }

  .brand { position: absolute; text-align: center; }
  .brand-name {
    font-weight: 400; font-size: 22px; letter-spacing: 3px; text-transform: uppercase;
    display: flex; align-items: center; gap: 8px; justify-content: center; white-space: nowrap;
  }
  .brand-dot { width: 9px; height: 9px; border-radius: 50%; }
  .card-front .brand { right: 26px; top: 56px; color: var(--paper); }
  .card-front .brand-dot { background: var(--paper); }
  .card-back .brand { left: 28px; top: 140px; color: var(--ink); }
  .card-back .brand-dot { background: var(--ink); }

  .contact { position: absolute; left: 26px; top: 196px; color: var(--paper); font-size: 12.5px; font-weight: 300; line-height: 18px; }
  .contact-address { border-left: 3px solid var(--paper); padding-left: 8px; margin-bottom: 4px; }
  .contact-line { display: flex; align-items: center; gap: 7px; padding-left: 11px; white-space: nowrap; }
  .contact-line svg { width: 11px; height: 11px; flex: none; }

  .ideas { position: absolute; right: 22px; top: 92px; list-style: none; text-align: right; font-size: 13px; line-height: 18px; color: var(--ink); }
  .ideas li { display: flex; justify-content: flex-end; align-items: center; gap: 8px; white-space: nowrap; }
  .ideas li::after { content: ""; width: 8px; height: 8px; border-radius: 50%; background: var(--bronze); flex: none; }
</style>
</head>
<body>
<main class="canvas">

  <section class="card card-front" aria-label="Card front">
    <svg class="waves" viewBox="0 0 560 320" aria-hidden="true">
      <path fill="var(--bronze)" d="M288,-12 L560,-12 L560,175 C505,195 480,265 455,320 L-12,320 L-12,168 C108,158 178,118 213,68 C238,28 258,-2 288,-12 Z"/>
      <path fill="var(--ink)" d="M300,0 L560,0 L560,175 C505,195 480,265 455,320 L0,320 L0,182 C120,172 190,130 225,80 C250,40 270,10 300,0 Z"/>
      <path fill="var(--bronze)" d="M560,168 C500,188 474,260 448,320 L455,320 C480,265 505,195 560,175 Z"/>
    </svg>

    <div class="holder">
      <div class="holder-name">Jess Holloran</div>
      <div class="holder-role">Owner</div>
    </div>

    <div class="brand">
      <div class="brand-name"><span class="brand-dot"></span>Morrel Wick Co</div>
    </div>

    <div class="contact">
      <div class="contact-address">Saltmarsh Bay, NSW Australia A small<br>wax studio, in a shed, by the bay</div>
      <div class="contact-line">
        <svg viewBox="0 0 12 12"><path fill="none" stroke="currentColor" stroke-width="1.3" d="M2.5,1 L4.5,1 L5.5,3.5 L4.2,4.5 C4.8,6 6,7.2 7.5,7.8 L8.5,6.5 L11,7.5 L11,9.5 C11,10.5 10,11 9,11 C5,10.5 1.5,7 1,3 C1,2 1.5,1 2.5,1 Z"/></svg>
        0481 572 316
      </div>
      <div class="contact-line">
        <svg viewBox="0 0 12 12"><rect x="1" y="2.5" width="10" height="7" fill="none" stroke="currentColor" stroke-width="1.2"/><path d="M1,2.5 L6,7 L11,2.5" fill="none" stroke="currentColor" stroke-width="1.2"/></svg>
        morrelwickco@mailbox.example.au
      </div>
      <div class="contact-line">
        <svg viewBox="0 0 12 12"><circle cx="6" cy="6" r="4.5" fill="currentColor"/></svg>
        friendspace.example.au/morrelwickco
      </div>
      <div class="contact-line">
        <svg viewBox="0 0 12 12"><circle cx="6" cy="6" r="5" fill="none" stroke="currentColor" stroke-width="1.1"/><path d="M1,6 H11 M6,1 C3,4 3,8 6,11 M6,1 C9,4 9,8 6,11" fill="none" stroke="currentColor" stroke-width="0.9"/></svg>
        craftlane.example/au/shop/MorrelWickCo
      </div>
    </div>
  </section>

  <section class="card card-back" aria-label="Card back">
    <svg class="waves" viewBox="0 0 560 320" aria-hidden="true">
      <path fill="var(--bronze)" d="M0,0 L560,0 L560,38 C430,42 350,92 230,82 C140,74 70,52 0,66 Z"/>
      <path fill="var(--ink)" d="M0,0 L560,0 L560,30 C430,34 350,84 230,74 C140,66 70,44 0,58 Z"/>
      <path fill="var(--bronze)" d="M0,320 L560,320 L560,232 C480,236 420,280 310,276 C200,272 120,300 0,290 Z"/>
      <path fill="var(--ink)" d="M0,320 L560,320 L560,240 C480,244 420,288 310,284 C200,280 120,308 0,298 Z"/>
    </svg>

    <div class="brand">
      <div class="brand-name"><span class="brand-dot"></span>Morrel Wick Co</div>
    </div>

    <ul class="ideas">
      <li>A Vase to Display fresh flowers</li>
      <li>Lolly Jar for your favourite candy</li>
      <li>Decorate with baubles at Christmas</li>
      <li>Bathroom Vanity Storage</li>
      <li>Decorate with eggs at Easter</li>
      <li>Plant a teranium inside.</li>
    </ul>
  </section>

</main>
</body>
</html>
```